Flyer-Design für Werbeflyer Teamentwicklung/Coaching als pdf
Zielgruppe
ich berate Personen, Teams und Organisationseinheiten, überwiegend im Profitbereich. (Internationale Konzerne). Mein Beratungsspektrum ist Führung, Prozessverbesserungen, Teamentwicklung
Aufgabenstellung
Der Text ist in Anlehnung an meine HP, Teamentwicklung und Coaching und es sollte eine übersichtliche, infomative 1-2 Seiten entstehen, die ich als erste Werbung/Kontaktaufnahme versenden kann. Die Seiten sollen klar einen Überblick über mein "Schaffen" geben, sollen aber auch schon etwas von meiner Arbeitsweise deutlich machen. (Ich begriefe schnell, formuliere klar und arbeite sehr zielorientiert - allerdings auch schnörkellos!) Diese Seiten sollten überwiegend als Anhang an eine Mail fungieren, im Ausnahmefall aber auch versendet werden.
Das Logo, die Farbe, etc. analog zu meiner HP - ich lass mich da aber auch gern beraten, falls sie andere Ideen haben

```html
<!DOCTYPE html>
<html lang="de">
<head>
<meta charset="utf-8">
<title>Teamentwicklung – Miriam Kessler</title>
<link rel="stylesheet" href="https://fonts.googleapis.com/css2?family=Open+Sans:wght@300;400;600;700&display=swap">
<style>
  :root{
    --purple:#7a0a5c;
    --band:#bccfc9;
    --grey:#6b7072;
    --text:#6f7375;
    --mark:#95a5a6;
    --fold:#e04fd0;
    --frame:#111;
  }
  *{box-sizing:border-box;margin:0;padding:0}
  html,body{width:1200px;height:849px;overflow:hidden;background:#fff}
  body{position:relative;font-family:"Open Sans",Arial,sans-serif;color:var(--text)}
  .spread{position:absolute;left:51px;width:1100px;height:389px;border:2px solid var(--frame);overflow:hidden;background:#fff}
  .spread--outside{top:20px}
  .spread--inside{top:441px}
  .band{position:absolute;top:12px;height:53px;background:var(--band)}
  .brand{position:absolute;top:12px;height:53px;width:56px;background:#fff;display:flex;flex-direction:column;align-items:center;justify-content:center;gap:3px}
  .brand__dot{width:14px;height:14px;border-radius:50%;background:var(--mark)}
  .brand__name{font-size:7px;font-weight:600;color:var(--mark);letter-spacing:.3px}
  .purple{position:absolute;background:var(--purple)}
  .fold{position:absolute;left:548px;top:0;bottom:0;border-left:1px dashed var(--fold)}
  .contact{position:absolute;left:400px;top:0;width:128px;height:138px;background:var(--purple);color:#fff;font-size:10px;line-height:11.6px;padding:13px 0 0 14px;font-style:normal}
  .contact p{margin-bottom:11px}
  .motto{position:absolute;left:175px;width:200px;text-align:center;font-weight:300;text-transform:uppercase}
  .motto .s{font-size:15.5px;color:var(--grey);display:block}
  .motto .l{font-size:28px;color:var(--purple);display:block;line-height:30px}
  .q{font-weight:700;font-size:15px;color:var(--grey)}
  .title{position:absolute;right:81px;top:92px;text-align:right;color:var(--grey);font-weight:600}
  .title__main{font-size:18.5px;letter-spacing:.6px;line-height:20px}
  .title__sub{font-size:15.5px;letter-spacing:.4px;line-height:18px}
  .title__sub b{color:var(--purple);font-weight:700}
  .photo{position:absolute}
  .photo--pier{left:548px;top:138px;width:552px;height:216px;background:linear-gradient(180deg,#8fb5dc 0%,#c9dbe8 35%,#5f7d86 52%,#7a7670 70%,#5b5650 100%)}
  .photo--hiker{left:390px;top:0;width:159px;height:389px;background:linear-gradient(180deg,#d9e2e3 0%,#b9c9c8 25%,#6f8a7e 50%,#6d6b5d 75%,#4f4a42 100%)}
  .band-quote{position:absolute;left:21px;top:21px;text-transform:uppercase;color:var(--purple);font-size:9.5px;line-height:18px}
  .band-quote .w{color:#fff;font-weight:300;font-size:16px}
  h2{position:absolute;font-size:16px;font-weight:700;color:var(--grey);letter-spacing:.5px}
  h3{position:absolute;font-size:8.5px;font-weight:700;color:var(--grey)}
  .copy{position:absolute;font-size:8.3px;line-height:10.2px;color:var(--text);hyphens:auto;-webkit-hyphens:auto}
  .copy p{margin-bottom:10px}
  .list{list-style:none}
  .list li{position:relative;padding-left:12px;margin-bottom:4px}
  .list li::before{content:"";position:absolute;left:0;top:2.5px;width:5px;height:5px;background:var(--purple)}
  .overlay{position:absolute;left:401px;top:212px;width:132px;height:154px;background:rgba(255,255,255,.55);border:1px solid rgba(255,255,255,.8);overflow:hidden}
  .overlay__label{position:absolute;left:3px;bottom:5px;writing-mode:vertical-rl;transform:rotate(180deg);color:var(--purple);font-size:13px;letter-spacing:.4px}
  .overlay__text{position:absolute;left:25px;top:4px;width:104px;font-size:8.9px;line-height:10.5px;color:#555;hyphens:auto;-webkit-hyphens:auto}
  .coach-quote{position:absolute;left:752px;top:74px;width:290px;text-align:center;text-transform:uppercase;font-size:7.5px;color:var(--grey);line-height:27.5px}
  .coach-quote .l{font-size:14px;color:var(--purple);font-weight:400}
  .coach-quote .src{display:block;font-size:4.5px;line-height:8px;text-transform:none}
</style>
</head>
<body>

<section class="spread spread--outside">
  <div class="band" style="left:0;width:400px"></div>
  <div class="band" style="left:528px;width:504px"></div>
  <div class="band" style="left:1082px;width:18px"></div>
  <div class="brand" style="left:24px"><span class="brand__dot"></span><span class="brand__name">KESSLER</span></div>
  <div class="brand" style="left:576px"><span class="brand__dot"></span><span class="brand__name">KESSLER</span></div>

  <address class="contact">
    <p>Miriam Kessler</p>
    <p>Lindenhof<br>Lindenweg 14-16<br>90402 Musterstadt</p>
    <p style="margin:0">Tel:&nbsp; 0911 - 12 34 56<br>Fax: 0911 - 1 23 45 67<br>info@miriam-kessler.de<br>www.miriam-kessler.de</p>
  </address>

  <div class="motto" style="top:112px">
    <span class="s"><span class="q">„</span> Die eigentliche</span>
    <span class="l" style="margin-top:6px">Entdeckung</span>
    <span class="s" style="margin-top:9px">besteht nicht darin,</span>
    <span class="l" style="margin-top:4px">Neuland</span>
    <span class="s" style="margin-top:1px">zu betreten,</span>
    <span class="s" style="margin-top:14px">sondern mit neuen</span>
    <span class="l" style="margin-top:1px">Augen</span>
    <span class="s" style="margin-top:2px">zu sehen.<span class="q">“</span></span>
  </div>

  <div class="fold"></div>
  <div class="purple" style="left:1032px;top:0;width:50px;height:104px"></div>

  <div class="title">
    <div class="title__main">TEAMENTWICKLUNG</div>
    <div class="title__sub">MIRIAM <b>KESSLER</b></div>
  </div>

  <div class="photo photo--pier" role="img" aria-label="Foto: Holzsteg mit Geländer, der über das Wasser zum Strand führt, blauer Himmel mit Wolken"></div>
</section>

<section class="spread spread--inside">
  <div class="purple" style="left:21px;top:0;width:50px;height:105px"></div>
  <div class="band" style="left:0;width:390px"></div>
  <div class="band-quote">
    „zu <span class="w">Erkennen</span> was geschieht,<br>
    ist der Beginn der <span class="w">Veränderung.“</span>
  </div>

  <h2 style="left:21px;top:150px">SEMINARE</h2>
  <div class="copy" style="left:21px;top:180px;width:160px">
    <p>In auf spezielle Themen ausgerichteten Seminaren finde ich mit Ihnen Strategien, um wiederkehrende Situationen positiv für Sie oder Ihr Unternehmen zu nutzen.</p>
  </div>
  <h2 style="left:21px;top:262px">ANGEBOT</h2>
  <div class="copy" style="left:21px;top:290px;width:160px">
    <p>Erfolgreiches Fehlermanagement durch konstruktive Kommunikation</p>
  </div>

  <h2 style="left:205px;top:87px">TEAMENTWICKLUNG</h2>
  <h3 style="left:205px;top:134px">DAZU GEHÖREN</h3>
  <ul class="copy list" style="left:205px;top:154px;width:145px">
    <li>Eine sorgfältige Analyse der Situation und Festlegung gewünschter Resultate</li>
    <li>Überzeugende und förderliche Methoden, die die Lösungskompetenzen der Menschen im Team unterstützen</li>
    <li>Klare Führung durch den Widerstreit von Teaminteressen zwischen Verändern, Bewahren, Harmonie und Konfliktbearbeitung, klarem Feedback und Eintracht im Team</li>
    <li>Tragfähigkeit der Ergebnisse</li>
  </ul>

  <div class="photo photo--hiker" role="img" aria-label="Foto: Wanderer mit Rucksack steht mit ausgebreiteten Armen auf einem Felsen über einer weiten Landschaft"></div>
  <div class="overlay">
    <span class="overlay__label">TEAMENTWICKLUNG</span>
    <p class="overlay__text">Teams sind lebendige Gebilde, die um erfolgreich zu sein, sich immer wieder neu ausrichten und koordinieren müssen. Das tun sie in aller Regel ohne fremde Hilfe - aber ab und zu ist es hilfreich, Impulse oder Entwicklungsförderung von außen bekommen.</p>
  </div>

  <div class="fold"></div>

  <div class="band" style="left:549px;width:483px"></div>
  <div class="band" style="left:1082px;width:18px"></div>
  <div class="brand" style="left:576px"><span class="brand__dot"></span><span class="brand__name">KESSLER</span></div>
  <div class="purple" style="left:1032px;top:0;width:50px;height:105px"></div>

  <h2 style="left:576px;top:87px">COACHING</h2>
  <div class="coach-quote">
    <span class="q" style="font-size:9px">„</span> Das wunderbare am <span class="l">Menschen</span> ist,<br>
    dass er wohl <span class="l">derselbe</span> bleibt,<br>
    aber nicht der <span class="l">Gleiche.</span><span class="q" style="font-size:9px">“</span>
    <span class="src" style="margin-left:30px">Friedrich Wendel, Schriftsteller, 1831-1910</span>
  </div>

  <div class="copy" style="left:584px;top:190px;width:155px">
    <p>Business-Coaching ist die professionelle Beratung und Begleitung, um Ihre beruflichen Ziele zu erreichen. Diese Form der Beratung wendet sich an Führungskräfte und andere Potentialträger in Organisationen und an Selbstständige.</p>
    <p>Coaching wirkt am besten, wenn berufliche Fragen nur eine einzelne Person betreffen, die sich konzentriert, zielgerichtet und zügig selbst verändern will.</p>
    <p>Schon wenige Termine, manchmal auch nur eine intensive Sitzung, reichen aus,</p>
  </div>
  <div class="copy" style="left:761px;top:190px;width:155px">
    <p>um eine Entwicklung auszulösen. Das Lernen geschieht bewusst und ganz konkret am jeweiligen Thema. Erfolgreiches Coaching lebt von gegenseitigem Vertrauen und Respekt.</p>
    <p>Ich verstehen meine Aufgabe darin, Ihnen durch geeignete Methoden und intelligente Gesprächsführung neue Perspektiven zu eröffnen – kurz, Sie dabei zu unterstützen, sich weiterzuentwickeln, Ihre Leistungsfähigkeit zu steigern und nach Ihren Maßstäben erfolgreich zu arbeiten.</p>
  </div>
  <ul class="copy list" style="left:932px;top:190px;width:160px">
    <li>für eine festgelegte Zeit durch einen beruflichen Sparringspartner eine andere Sichtweise kennen zu lernen, so dass neue Perspektiven entstehen</li>
    <li>Stärkung der Führungsqualitäten</li>
    <li>Führungsstil und Führungsrolle</li>
    <li>Mitarbeiterführung</li>
    <li>Kooperationsstrategien</li>
    <li>Stärkenprofil, persönliches Potenzial</li>
    <li>einen latenten oder akuten Konflikt dauerhaft lösen zu wollen</li>
    <li>Karriereplanung</li>
    <li>Burn-out-Prophylaxe</li>
  </ul>
</section>

</body>
</html>
```